Tax Preparation flyer for LedgerMint Corp.

My Client would like a one page PDF flyer to promote upcoming tax season in Canada. This firm is affordable and all virtual. I have attached a copy of their logo and a word document with the proposed wording for the flyer. Please feel free to change if you have better suggestions.

Target Market(s)

individuals in canada

Colors
0054AA
0677BA
7BADD7
CADEEF
E8F1F8

```html
<!DOCTYPE html>
<html lang="en">
<head>
<meta charset="utf-8">
<title>LedgerMint Corp. – Tax Season Flyer</title>
<link rel="stylesheet" href="https://fonts.googleapis.com/css2?family=Poppins:wght@400;500;600;700;800&display=swap">
<style>
  :root{
    --blue:#1b98d8;
    --slate:#40657c;
    --charcoal:#343638;
    --ink:#3a3a3a;
    --grey-overlay:#6e6f70;
    --backdrop:#e6e7e9;
    --white:#ffffff;
  }
  *{margin:0;padding:0;box-sizing:border-box}
  html,body{width:1200px;height:1200px;overflow:hidden;background:var(--backdrop)}
  body{position:relative;font-family:'Poppins',sans-serif;color:var(--ink)}
  .flyer{position:absolute;left:202px;top:42px;width:795px;height:1115px;background:var(--white);overflow:hidden}
  .flyer-shapes{position:absolute;left:0;top:0;width:795px;height:1115px}
  .abs{position:absolute}
  .line{display:block;white-space:nowrap}
  .headline{right:33px;top:14px;font-size:98px;font-weight:700;color:var(--blue);line-height:1;letter-spacing:-1px}
  .subheadline{right:26px;top:104px;font-size:32px;font-weight:500;color:var(--ink);line-height:1.2;white-space:nowrap}
  .intro{right:26px;top:160px;text-align:right;font-size:12.2px;line-height:19.5px}
  .hl{color:var(--blue);font-weight:700}
  .body-copy{left:27px;font-size:12.2px;line-height:19.5px}
  .portal-note{top:655px}
  .meeting-strip{left:27px;top:699px;height:26px;line-height:26px;font-size:12.2px;font-weight:700;color:var(--white);white-space:nowrap}
  .pricing-box{left:189px;top:752px;width:421px;height:83px;background:var(--charcoal);border-radius:6px}
  .pricing-tab{left:270px;top:741px;width:256px;height:38px}
  .pricing-title{left:270px;top:740px;width:256px;text-align:center;font-size:29px;font-weight:700;color:var(--white);line-height:40px}
  .return-label{left:196px;top:783px;width:138px;text-align:center;font-size:12.4px;color:var(--white)}
  .return-price{left:196px;top:797px;width:138px;text-align:center;font-size:31px;font-weight:700;color:var(--white);line-height:1.2}
  .schedule-box{left:337px;top:786px;width:264px;height:43px;background:var(--white);border-radius:5px;text-align:center;font-size:13px;line-height:19px;padding-top:3px;color:var(--ink)}
  .schedule-box b{font-weight:700}
  .complex-note{top:845px}
  .behind-title{left:0;top:890px;width:795px;text-align:center;font-size:16px;font-weight:700;color:var(--ink)}
  .save-box{left:82px;top:919px;width:630px;height:25px;border:1.5px solid var(--charcoal);border-radius:4px;box-shadow:2px 2px 0 var(--charcoal);text-align:center;font-size:12.4px;line-height:22px;white-space:nowrap}
  .refund-note{top:957px}
  .closing{left:27px;top:1000px;font-size:22px;font-weight:700;color:var(--ink);white-space:nowrap}
  .closing .accent{color:var(--blue)}
  .brand-name{right:26px;top:1012px;text-align:right;font-size:31px;font-weight:700;color:var(--charcoal);line-height:36px}
  .contact-title{left:28px;top:1041px;height:24px;line-height:26px;font-size:17px;font-weight:700;color:var(--white)}
  .contact-item{top:1070px;height:22px;display:flex;align-items:center;gap:7px;font-size:13.2px;color:var(--white)}
  .contact-item svg{width:18px;height:18px}
  .contact-email{left:27px}
  .contact-phone{left:203px}
</style>
</head>
<body>
<main class="flyer">
  <svg class="flyer-shapes" viewBox="0 0 1280 1794" preserveAspectRatio="none" aria-hidden="true">
    <defs>
      <linearGradient id="photoTone" x1="0" y1="0" x2="1" y2="1">
        <stop offset="0" stop-color="#f2f5f7"/>
        <stop offset="0.55" stop-color="#d9dee2"/>
        <stop offset="1" stop-color="#eef1f3"/>
      </linearGradient>
    </defs>
    <polygon points="0,0 86,0 349,400 0,400" fill="var(--blue)"/>
    <g role="img" aria-label="Photo: a man in a suit meditating calmly at his desk in front of a laptop in a bright office">
      <rect x="284" y="400" width="996" height="604" fill="url(#photoTone)"/>
    </g>
    <polygon points="0,125 124,125 284,400 134,1004 0,1004" fill="var(--slate)"/>
    <polygon points="284,400 720,1004 134,1004" fill="var(--grey-overlay)" opacity="0.85"/>
    <polygon points="0,1004 990,1004 1015,1037 0,1037" fill="var(--blue)"/>
    <polygon points="990,1004 1280,1004 1280,1037 1015,1037" fill="var(--charcoal)"/>
    <rect x="0" y="1125" width="1280" height="42" fill="var(--charcoal)"/>
    <polygon points="0,1676 268,1676 299,1714 0,1714" fill="var(--blue)"/>
    <polygon points="0,1716 536,1716 614,1794 0,1794" fill="var(--charcoal)"/>
    <polygon points="536,1716 568,1716 627,1794 614,1794" fill="var(--blue)"/>
  </svg>

  <h1 class="abs headline">Relax!</h1>
  <h2 class="abs subheadline">We’ve Got Your Taxes Covered!</h2>
  <p class="abs intro">
    <span class="line">Our tax preparers have over <span class="hl">20 years</span> experience and worked both in public accounting</span>
    <span class="line">firms as well as specialized tax.&nbsp; Our tax services are virtual, so you don’t have to take the</span>
    <span class="line">time for a personal visit. We take care of everything and can access all your tax slips</span>
    <span class="line">from CRA website directly into our tax software. All signing is done via <span class="hl">SignFlow</span>.</span>
  </p>

  <p class="abs body-copy portal-note">
    <span class="line">You can fill and submit the appropriate forms, along with all your other documents, in our secure client portal. It’s</span>
    <span class="line">important that we understand your situation and any changes in your situation from the past year.</span>
  </p>
  <p class="abs meeting-strip">If you have a complex tax situation and would like to discuss it, we can meet in virtually over Meetly or Convia.</p>

  <div class="abs pricing-box"></div>
  <svg class="abs pricing-tab" viewBox="0 0 256 38" aria-hidden="true">
    <path d="M0,12 Q8,0 20,2 L236,2 Q248,0 256,12 Z" fill="var(--slate)"/>
    <path d="M18,2 L238,2 Q226,36 196,36 L60,36 Q30,36 18,2 Z" fill="var(--blue)"/>
  </svg>
  <h3 class="abs pricing-title">Pricing</h3>
  <p class="abs return-label">Personal Tax Return</p>
  <p class="abs return-price">$100.00</p>
  <div class="abs schedule-box">Add a business or rental schedule<br><b>$125</b> per business or rental property.</div>

  <p class="abs body-copy complex-note">
    <span class="line">More complex tax returns will be assessed based on the complexity of the return and you will be advised before we</span>
    <span class="line">start.</span>
  </p>
  <h3 class="abs behind-title">Did you fall behind in <span class="hl">filing your income tax</span>?</h3>
  <p class="abs save-box">Save <span class="hl">20%</span> when you file <span class="hl">3 or more</span> years with us.&nbsp; We can do <span class="hl">back to 2012</span> for filing of tax returns.</p>
  <p class="abs body-copy refund-note">
    <span class="line">If you expect a refund, the earlier you file the sooner you will receive your refund.&nbsp; Our average turn around time prior</span>
    <span class="line">to April is a couple of days.</span>
  </p>

  <p class="abs closing">So you can start <span class="accent">to breathe easy</span>.</p>
  <p class="abs brand-name">LedgerMint<br>Corp.</p>

  <p class="abs contact-title">Contact us:</p>
  <p class="abs contact-item contact-email">
    <svg viewBox="0 0 20 20" aria-hidden="true"><circle cx="10" cy="10" r="9" fill="none" stroke="#fff" stroke-width="1.3"/><rect x="5" y="6.5" width="10" height="7" fill="none" stroke="#fff" stroke-width="1.2"/><path d="M5,6.5 L10,10.5 L15,6.5" fill="none" stroke="#fff" stroke-width="1.2"/></svg>
    hello@ledgermint.ca
  </p>
  <p class="abs contact-item contact-phone">
    <svg viewBox="0 0 20 20" aria-hidden="true"><circle cx="10" cy="10" r="9" fill="none" stroke="#fff" stroke-width="1.3"/><path d="M7,5.5 L8.6,5.5 L9.3,8 L8.2,8.9 Q9.2,11 11.1,11.9 L12,10.8 L14.5,11.5 L14.5,13 Q14.2,14.5 12.5,14.4 Q6,13.5 5.6,7.3 Q5.6,5.7 7,5.5 Z" fill="none" stroke="#fff" stroke-width="1.1"/></svg>
    555 010 0199
  </p>
</main>
</body>
</html>
```